Carton Box Packaging For Motorcycle Brake Shoe - Varonel Brand

Packaging Dimensions: 125mm (H) x 125mm (W) x 31mm (D)
We would like to design a genuine Carton box Packaging for motorcycle Brake Shoe.
This is a critical part of the motorcycle, so we need the packaging to reflect elegant impression.
Varonel, is one of the leading companies for manufacturing Motorcycles, located in Egypt. Our company is offering high-quality products, the best in the local market, with very competitive prices.
We have a limited time to get this project done, So we Highly appreciate receiving your designs ASAP.
Target Market(s)
Economical Motorcycle Buyers
Colors
Designer to choose colors to be used in the design.
Look and feel

```html
<!DOCTYPE html>
<html lang="en">
<head>
<meta charset="utf-8">
<title>Varonel Motorcycle Brake Shoe Carton</title>
<link href="https://fonts.googleapis.com/css2?family=Tinos&display=swap" rel="stylesheet">
<style>
  :root {
    --red: #ed1c24;
    --blue: #0c55a5;
    --ink: #333333;
    --fold: #9a9a9a;
    --paper: #ffffff;
    --steel-light: #c9c9c9;
    --steel-dark: #5e5e58;
    --serif: "Tinos", "Times New Roman", serif;
  }
  * { box-sizing: border-box; margin: 0; padding: 0; }
  html, body { width: 696px; height: 1200px; overflow: hidden; background: var(--paper); }
  .dieline { position: relative; width: 696px; height: 1200px; font-family: var(--serif); color: var(--ink); }
  .panel { position: absolute; border: 1px solid var(--fold); background: var(--paper); overflow: hidden; }
  .stripes { position: absolute; background: linear-gradient(135deg, var(--red) 0%, #8c3a6c 50%, var(--blue) 100%); }
  .photo-shoe { position: absolute; border-radius: 50%; background: radial-gradient(circle, var(--paper) 38%, var(--steel-light) 42%, var(--steel-dark) 62%, #3c3c38 70%, transparent 71%); }
  .white-disc { position: absolute; border-radius: 50%; background: var(--paper); }
  .brand { position: absolute; display: flex; flex-direction: column; align-items: center; justify-content: center; gap: 6px; font-family: var(--serif); color: var(--ink); }
  .brand-dot { border-radius: 50%; background: #8a8a8a; }
  .label { position: absolute; background: var(--paper); display: flex; align-items: center; justify-content: center; text-align: center; font-family: var(--serif); color: var(--ink); line-height: 1; }

  /* front */
  .front .hero-disc { left: 92px; top: 29px; width: 242px; height: 242px; }
  .front .brand { left: 92px; top: 29px; width: 242px; height: 242px; font-size: 34px; gap: 10px; }
  .front .brand-dot { width: 70px; height: 70px; }
  .front .title-box { left: 53px; top: 304px; width: 320px; height: 99px; border-radius: 12px; justify-content: flex-start; }
  .front .title-box .photo-shoe { position: relative; flex: none; width: 84px; height: 80px; margin-left: 14px; }
  .front .title-text { font-size: 42px; line-height: 44px; margin-left: 12px; text-align: center; }

  /* band (top and bottom edges) */
  .band .stripes { left: 89px; top: 2px; width: 240px; height: 101px; }
  .band .brand { left: 6px; top: 4px; width: 82px; height: 98px; font-size: 15px; }
  .band .brand-dot { width: 52px; height: 52px; }
  .band .end-disc { left: 311px; top: -5px; width: 116px; height: 116px; }
  .band .photo-shoe { left: 322px; top: 6px; width: 96px; height: 92px; }
  .band .tag { left: 149px; top: 24px; width: 120px; height: 47px; border-radius: 8px; font-size: 20px; line-height: 22px; }
  .flip { transform: rotate(180deg); }

  /* side panels */
  .side .stripes { left: 2px; top: 97px; width: 101px; height: 245px; }
  .side .disc-top { left: -8px; top: 48px; width: 120px; height: 90px; }
  .side .disc-bottom { left: -8px; top: 318px; width: 120px; height: 90px; }
  .side .photo-shoe { left: 10px; top: 6px; width: 90px; height: 96px; }
  .side .brand { left: 4px; top: 342px; width: 98px; height: 84px; flex-direction: row; font-size: 15px; }
  .side .brand-dot { width: 50px; height: 50px; }
  .side .brand-name { writing-mode: vertical-rl; transform: rotate(180deg); }
  .side .tag { left: 28px; top: 158px; width: 50px; height: 120px; border-radius: 8px; }
  .side .tag-text { transform: rotate(-90deg); white-space: nowrap; font-size: 20px; line-height: 22px; text-align: center; }

  /* back */
  .info-box { position: absolute; left: 102px; top: 104px; width: 220px; height: 221px; border: 1px solid var(--ink); border-radius: 10px; display: flex; flex-direction: column; align-items: center; justify-content: center; font-size: 12.5px; line-height: 17.5px; text-align: center; }
  .info-gap { height: 17px; }
</style>
</head>
<body>
<main class="dieline">
  <!-- top tuck flap and dust flaps -->
  <div class="panel" style="left:134px;top:0;width:426px;height:107px;"></div>
  <div class="panel" style="left:28px;top:6px;width:106px;height:96px;"></div>
  <div class="panel" style="left:560px;top:6px;width:105px;height:96px;"></div>

  <!-- front -->
  <section class="panel front" style="left:134px;top:107px;width:426px;height:430px;">
    <div class="stripes" role="img" aria-label="Red and blue diagonal stripe pattern" style="left:0;top:8px;width:426px;height:413px;"></div>
    <div class="white-disc hero-disc"></div>
    <div class="brand"><span class="brand-dot"></span><span class="brand-name">Varonel</span></div>
    <div class="label title-box">
      <div class="photo-shoe" role="img" aria-label="Photo of a motorcycle brake shoe pair"></div>
      <p class="title-text">motorcycle<br>brake shoe</p>
    </div>
  </section>
  <div class="panel" style="left:28px;top:107px;width:106px;height:430px;"></div>
  <div class="panel" style="left:560px;top:107px;width:105px;height:430px;"></div>

  <!-- top band -->
  <section class="panel band" style="left:134px;top:537px;width:426px;height:106px;">
    <div class="stripes" role="img" aria-label="Red and blue diagonal stripe pattern"></div>
    <div class="white-disc end-disc"></div>
    <div class="photo-shoe" role="img" aria-label="Photo of a motorcycle brake shoe pair"></div>
    <div class="brand"><span class="brand-dot"></span><span>Varonel</span></div>
    <div class="label tag">motorcycle<br>brake shoe</div>
  </section>
  <div class="panel" style="left:28px;top:542px;width:106px;height:96px;"></div>
  <div class="panel" style="left:560px;top:542px;width:105px;height:96px;"></div>

  <!-- left side -->
  <section class="panel side" style="left:28px;top:643px;width:106px;height:431px;">
    <div class="stripes" role="img" aria-label="Red and blue diagonal stripe pattern"></div>
    <div class="white-disc disc-top"></div>
    <div class="white-disc disc-bottom"></div>
    <div class="photo-shoe" role="img" aria-label="Photo of a motorcycle brake shoe pair"></div>
    <div class="label tag"><p class="tag-text">motorcycle<br>brake shoe</p></div>
    <div class="brand"><span class="brand-dot"></span><span class="brand-name">Varonel</span></div>
  </section>

  <!-- back -->
  <section class="panel back" style="left:134px;top:643px;width:426px;height:431px;">
    <div class="info-box">
      <p>Part name</p>
      <p>Part code</p>
      <div class="info-gap"></div>
      <p>Manufacturer name</p>
      <p>Manufacturer address</p>
      <p>Manufacturer phone</p>
    </div>
  </section>

  <!-- right side -->
  <section class="panel side flip" style="left:560px;top:643px;width:105px;height:431px;">
    <div class="stripes" role="img" aria-label="Red and blue diagonal stripe pattern"></div>
    <div class="white-disc disc-top"></div>
    <div class="white-disc disc-bottom"></div>
    <div class="photo-shoe" role="img" aria-label="Photo of a motorcycle brake shoe pair"></div>
    <div class="label tag"><p class="tag-text">motorcycle<br>brake shoe</p></div>
    <div class="brand"><span class="brand-dot"></span><span class="brand-name">Varonel</span></div>
  </section>

  <!-- bottom band -->
  <section class="panel band flip" style="left:134px;top:1074px;width:426px;height:107px;">
    <div class="stripes" role="img" aria-label="Red and blue diagonal stripe pattern"></div>
    <div class="white-disc end-disc"></div>
    <div class="photo-shoe" role="img" aria-label="Photo of a motorcycle brake shoe pair"></div>
    <div class="brand"><span class="brand-dot"></span><span>Varonel</span></div>
    <div class="label tag">motorcycle<br>brake shoe</div>
  </section>
</main>
</body>
</html>
```